Brill Insurance Agency - Business Cards

Hello, I am needing new trendy business cards for our Insurance Agency now that I have a new Logo. I have attached our new logo with several color options along with a business card design that I like. I am leaning towards burgundy and blue colors. I have attached our current business card. I have also attached a headshot of our company president, Martin Vale, that you can use if you wish. Thank you so much in advance for all the wonderful designs!!!!

Target Market(s)

We want to look very professional to potential customers and we also want to look very professional so insurance companies will want to contract with us to sell their product.

Industry/Entity Type

Insurance

Contact Information for Business Card

Martin Vale
mvale@brillagency.com
Business: 555-213-4087
Fax: 555-213-7751
Cell: 555-390-2618
Toll Free: 888-555-0194
42 W Elm Rd Butler, MO 64730
www.brillagency.net

Font styles to use
Serif
Sans Serif

Colors
0355a3
3277b5
f04a50
ec1f27

Requirements
Nice to have
• I love creativity. The more creative and balanced a business card design the more I will like it. I would like the card to be printed horizontally instead of vertically.
Should not have
• My project should not have the Allied Coverage Network logo. It is no longer used in the industry.

```html
<!DOCTYPE html>
<html lang="en">
<head>
<meta charset="utf-8">
<title>Brill Insurance Agency – Business Cards</title>
<link rel="stylesheet" href="https://fonts.googleapis.com/css2?family=Montserrat:wght@400;500;600&display=swap">
<style>
  :root {
    --backdrop: #ececec;
    --brand-blue: #0355a3;
    --brand-blue-light: #3277b5;
    --brand-red: #ec1f27;
    --brand-red-soft: #f04a50;
    --paper: #ffffff;
    --ink-light: #ffffff;
  }
  * { margin: 0; padding: 0; box-sizing: border-box; }
  html, body {
    width: 1200px; height: 800px; overflow: hidden;
    background: var(--backdrop);
    font-family: "Montserrat", Arial, sans-serif;
  }
  .stage { position: relative; width: 1200px; height: 800px; }

  .card {
    position: absolute; top: 278px; width: 420px; height: 240px;
    overflow: hidden;
  }
  .card--front { left: 141px; background: var(--brand-blue); }
  .card--back  { left: 637px; background: var(--paper); }

  .lockup { position: absolute; display: flex; align-items: center; gap: 32px; }
  .lockup__dot { flex: none; }
  .lockup__name {
    font-weight: 600; line-height: 1.2; letter-spacing: 0.02em;
    text-transform: uppercase; white-space: nowrap;
  }
  .lockup__line2 { display: block; font-size: 0.68em; letter-spacing: 0.22em; text-align: center; }

  .card--front .lockup { left: 76px; top: 94px; }
  .card--front .lockup__name { color: var(--ink-light); font-size: 18px; }

  .card--back .lockup { left: 74px; top: 29px; }
  .card--back .lockup__name { color: var(--brand-blue); font-size: 17px; }

  .contact-band {
    position: absolute; left: 0; top: 104px; width: 100%; height: 80px;
    background: var(--brand-blue); color: var(--ink-light);
  }
  .contact-band__person {
    position: absolute; left: 20px; top: 12px; width: 134px; text-align: right;
  }
  .person-name {
    font-size: 15px; font-weight: 500; letter-spacing: 0.04em;
    text-transform: uppercase; text-align: left; padding-left: 11px; margin-bottom: 8px;
  }
  .person-links { font-size: 11px; line-height: 14px; white-space: nowrap; }
  .contact-band__divider {
    position: absolute; left: 180px; top: 14px; width: 1px; height: 50px;
    background: var(--ink-light);
  }
  .contact-band__numbers {
    position: absolute; left: 210px; top: 12px;
    list-style: none; font-size: 11px; line-height: 14px; white-space: nowrap;
  }

  .address-band {
    position: absolute; left: 0; top: 196px; width: 100%; height: 30px;
    background: var(--brand-red); color: var(--ink-light);
    font-size: 12px; line-height: 30px; text-align: center;
  }
</style>
</head>
<body>
<main class="stage">

  <section class="card card--front" aria-label="Card front">
    <div class="lockup">
      <svg class="lockup__dot" width="54" height="54" viewBox="0 0 54 54" aria-hidden="true">
        <circle cx="27" cy="27" r="24" fill="none" stroke="#ffffff" stroke-width="5"/>
      </svg>
      <p class="lockup__name">Brill Insurance<span class="lockup__line2">Agency Inc</span></p>
    </div>
  </section>

  <section class="card card--back" aria-label="Card back">
    <div class="lockup">
      <svg class="lockup__dot" width="54" height="54" viewBox="0 0 54 54" aria-hidden="true">
        <circle cx="27" cy="27" r="24" fill="none" stroke="#f04a50" stroke-width="5"/>
      </svg>
      <p class="lockup__name">Brill Insurance<span class="lockup__line2">Agency Inc</span></p>
    </div>

    <div class="contact-band">
      <div class="contact-band__person">
        <p class="person-name">Martin Vale</p>
        <p class="person-links">mvale@brillagency.com<br>www.brillagency.net</p>
      </div>
      <span class="contact-band__divider"></span>
      <ul class="contact-band__numbers">
        <li>Business: 555-213-4087</li>
        <li>Fax: 555-213-7751</li>
        <li>Cell: 555-390-2618</li>
        <li>Toll Free: 888-555-0194</li>
      </ul>
    </div>

    <p class="address-band">42 W Elm Rd Butler, MO 64730</p>
  </section>

</main>
</body>
</html>
```